Medical Call Centre Needs a Web Design

We need a web design for a new company based in Melbourne called "Clinora Services". We provide medical centres with administrative support by managing inbound calls to our clients facility. We require a clean, simple and easy to navigate website with an ultimate end product alike this - http://www.plumevanta.com/

The final design should communicate professionalism, new age and inovative.

Industry/Entity Type

It Company

```html
<!DOCTYPE html>
<html lang="en">
<head>
<meta charset="utf-8">
<title>Clinora Services</title>
<link rel="stylesheet" href="https://fonts.googleapis.com/css2?family=Oswald:wght@300;400&family=Open+Sans:wght@400;600;700&display=swap">
<style>
:root{
  --red:#c8102e;
  --red-dark:#a50d25;
  --ink:#2b2b2b;
  --dark:#2f2f31;
  --darker:#1c1c1e;
  --grey:#ebebeb;
  --white:#ffffff;
  --muted:#555555;
  --line:#444444;
}
*{margin:0;padding:0;box-sizing:border-box}
html,body{width:1200px;height:2704px;overflow:hidden}
body{font-family:"Open Sans",Arial,sans-serif;color:var(--ink);background:var(--white);font-size:15px;line-height:1.6}
.section-title{font-family:"Oswald",Arial,sans-serif;font-weight:300;font-size:52px;letter-spacing:1px;text-align:center;line-height:1}
.wrap{width:880px;margin:0 auto}

/* header + hero */
.hero{position:relative;height:660px;background:linear-gradient(180deg,#f4f4f4 0%,#d9d9d9 100%);overflow:hidden}
.hero-photo{position:absolute;right:0;top:0;width:660px;height:660px;background:radial-gradient(circle at 60% 45%,#f0cdb4 0%,#d9a987 30%,#c7c7c7 60%,#e4e4e4 100%)}
.brand{position:absolute;left:160px;top:0;width:120px;height:100px;background:var(--darker);color:var(--white);font-weight:700;font-size:18px;line-height:1.15;padding:18px 14px}
.call-us{position:absolute;right:40px;top:0;background:var(--darker);color:var(--white);font-weight:700;font-size:18px;padding:6px 24px;letter-spacing:.5px}
.nav{position:absolute;left:160px;top:112px;display:flex;background:rgba(60,60,60,.55)}
.nav a{display:block;color:var(--white);text-decoration:none;font-size:14px;font-weight:600;padding:12px 22px;text-transform:uppercase}
.nav a.active{background:var(--red)}
.hero-title{position:absolute;left:160px;top:350px;color:var(--white);font-weight:700;font-size:54px;line-height:1.12;text-shadow:0 2px 6px rgba(0,0,0,.35)}
.hero-sub{position:absolute;left:160px;top:526px;background:var(--red);color:var(--white);font-size:22px;padding:4px 18px}

/* about */
.about{height:220px;background:var(--red);color:var(--white);text-align:center;padding-top:36px;overflow:hidden}
.about p{width:860px;margin:24px auto 0;font-size:15px;line-height:1.55}

/* goal */
.goal{height:420px;padding-top:60px}
.goal-body{display:flex;justify-content:space-between;align-items:center;margin-top:50px}
.goal ol{padding-left:22px;font-size:17px;line-height:2.1}
.goal-image{width:240px;height:240px;background:radial-gradient(circle at 50% 50%,#b67f4f 0%,#8f5b31 55%,#ffffff 75%)}

/* overview */
.overview{height:400px;background:var(--grey);padding-top:44px}
.overview p{margin-top:30px;font-size:14.5px}
.overview p + p{margin-top:18px}
.concept{position:relative;height:80px;margin-top:28px;font-family:"Oswald",Arial,sans-serif;font-size:20px;letter-spacing:1px}
.concept span{position:absolute}
.concept .rule{position:absolute;height:2px;background:var(--line)}

/* benefits */
.benefits{height:420px;background:var(--dark);color:var(--white);padding-top:44px}
.benefits-body{display:flex;justify-content:space-between;margin-top:28px}
.benefits-text{width:640px;font-size:14px}
.benefits ul{margin:14px 0 14px 22px;line-height:1.75}
.dashboard{width:232px;height:252px;margin-top:20px;background:linear-gradient(180deg,#ffffff 0%,#e8eef4 100%);border:4px solid #d5d5d5}

/* contact */
.contact{height:480px;padding-top:72px;border-top:6px solid var(--red)}
.contact-body{display:flex;justify-content:space-between;margin-top:40px}
.contact-text{width:640px;font-size:14.5px}
.contact-text p + p{margin-top:16px}
.contact ul{margin:14px 0 0 22px;font-weight:700;line-height:1.7}
.contact-photo{width:240px;height:260px;margin-top:24px;background:radial-gradient(circle at 50% 40%,#f1d0b9 0%,#e9d6c9 45%,#ffffff 75%)}

/* footer */
.footer{height:104px;background:var(--darker);border-top:6px solid var(--red);color:#bbbbbb}
.footer-row{display:flex;align-items:center;justify-content:space-between;width:1040px;margin:0 auto;padding-top:14px}
.footer-nav{display:flex}
.footer-nav a{color:var(--white);text-decoration:none;font-size:13px;text-transform:uppercase;padding:8px 18px}
.footer-nav a.active{background:#3a3a3c}
.follow{display:flex;align-items:center;gap:8px;font-size:13px}
.follow i{display:block;width:26px;height:26px;background:#3d6f9e}
.follow i:nth-child(3){background:#3aa0d8}
.follow i:nth-child(4){background:#777777}
.copyright{text-align:center;font-size:12px;margin-top:16px}
</style>
</head>
<body>

<header class="hero">
  <div class="hero-photo" role="img" aria-label="Smiling call centre operator wearing a headset"></div>
  <div class="brand">Clinora<br>Services</div>
  <div class="call-us">CALL US ON - 1300-618-272</div>
  <nav class="nav">
    <a class="active" href="#">Home</a>
    <a href="#">About Us</a>
    <a href="#">Our Goal</a>
    <a href="#">Overview</a>
    <a href="#">Benefits</a>
    <a href="#">Contact Us</a>
  </nav>
  <h1 class="hero-title">Lorem ipsum dolor<br>sit amet, consectetur</h1>
  <div class="hero-sub">Lorem ipsum dolor sit amet, consectetur adipiscing elit</div>
</header>

<section class="about">
  <h2 class="section-title">ABOUT US</h2>
  <p>Clinora Services is an Australian owned company who will provide a support network to your administration team, working together by easing some of the daily distractions and managing your inbound calls. Acting as a switchboard for your organisation and providing exceptional customer service.</p>
</section>

<section class="goal">
  <div class="wrap">
    <h2 class="section-title">OUR GOAL</h2>
    <div class="goal-body">
      <ol>
        <li>Simple and easy to do business with</li>
        <li>Proactive and transparent with information, news and changes</li>
        <li>Best in-class and independently assessed</li>
        <li>Delivering a premium patient experience</li>
      </ol>
      <div class="goal-image" role="img" aria-label="Row of figures standing together with one highlighted"></div>
    </div>
  </div>
</section>

<section class="overview">
  <div class="wrap">
    <h2 class="section-title">OVERVIEW</h2>
    <p>Clinora Services aim to change the way medical facilities interact with patients, by assisting with the management of inbound calls – an industry initiative to encourage and support the growth of patient care and customer service.</p>
    <p>The medical industry over recent years has seen a growth in terms of service quality, efficiency, and availability. In addition, medical standards are evolving to embrace the use of IT within the medical industry.</p>
    <div class="concept">
      <span style="left:20px;top:0">CULTURE</span>
      <div class="rule" style="left:0;top:34px;width:330px"></div>
      <span style="left:340px;top:20px">ORGANIZATION</span>
      <div class="rule" style="left:490px;top:34px;width:390px"></div>
      <span style="left:620px;top:0">CHANGE</span>
      <span style="left:610px;top:42px">INITIATIVE</span>
    </div>
  </div>
</section>

<section class="benefits">
  <div class="wrap">
    <h2 class="section-title">BENEFITS</h2>
    <div class="benefits-body">
      <div class="benefits-text">
        <p>Clinora Services will allow you to explore unmeasured communication activities currently unmonitored by your facility. Now you can consider the following:</p>
        <ul>
          <li>Volume</li>
          <li>Talk time</li>
          <li>Queue time</li>
          <li>Abandoned calls</li>
          <li>Quality assurance</li>
        </ul>
        <p>By utilising our service, we will enable your facility to enhance efficiency and identify trends and resources required to offer the best possible service within the medical industry. Calibrate and conduct evidence based decision making and take time to understand your callers.</p>
      </div>
      <div class="dashboard" role="img" aria-label="Call statistics dashboard with gauges and a line chart"></div>
    </div>
  </div>
</section>

<section class="contact">
  <div class="wrap">
    <h2 class="section-title">CONTACT US</h2>
    <div class="contact-body">
      <div class="contact-text">
        <p>Clinora Services will manage a diverted telecommunications environment through the professional management of inbound calls to your facility. Having developed tailored protocols and message scripts, we will provide a consistent level of service, giving callers the direction they deserve without interruption.</p>
        <p>Providing exceptional supportive services with a primary focus in the following categories:</p>
        <ul>
          <li>General Enquiries</li>
          <li>Account Enquiries</li>
          <li>Appointments</li>
          <li>Results</li>
          <li>Internal</li>
        </ul>
      </div>
      <div class="contact-photo" role="img" aria-label="Receptionist with headset ready to take calls"></div>
    </div>
  </div>
</section>

<footer class="footer">
  <div class="footer-row">
    <nav class="footer-nav">
      <a class="active" href="#">Home</a>
      <a href="#">About Us</a>
      <a href="#">Our Goal</a>
      <a href="#">Overview</a>
      <a href="#">Benefits</a>
      <a href="#">Contact Us</a>
    </nav>
    <div class="follow"><span>Follow us</span><i></i><i></i><i></i></div>
  </div>
  <p class="copyright">Privacy | Copyright</p>
</footer>

</body>
</html>
```